letterhead design using our existing logo

We are a small boutique property management business based in Sydney's Northern Beaches.
We are after a sleek, simple modern letterhead (A4) incorporating our logo and its colours.
Also matching envelope (DL)
I have attached the logo with black text and white text for design options.

Target Market(s)

29-69yo Male and Female

Industry/Entity Type

Property Management

Requirements
Must have
• - Keyhaven Estates logo
• - Address, number and website:
• Suite 7, 18-19 Harlow Parade, Brookvale NSW 2100
• Tel: Tom Carrick 0417 293 608 Lorena Adcock 0409 516 742 www.keyhavenestatesgroup.com.au
Nice to have
• sleek design that looks modern and professional
Should not have
• too many colours or too busy

```html
<!DOCTYPE html>
<html lang="en">
<head>
<meta charset="utf-8">
<title>Keyhaven Estates – Letterhead</title>
<link rel="stylesheet" href="https://fonts.googleapis.com/css2?family=Open+Sans:wght@400;600&display=swap">
<style>
  :root {
    --backdrop: #b9b9b9;
    --paper: #ffffff;
    --ink: #1b1b1b;
    --ink-soft: #2f3a3d;
    --brand-teal: #2b8c91;
    --tint-pale: #d3e1e4;
  }
  * { box-sizing: border-box; margin: 0; padding: 0; }
  html, body {
    width: 960px;
    height: 1200px;
    overflow: hidden;
    background: var(--backdrop);
  }
  .canvas {
    position: relative;
    width: 960px;
    height: 1200px;
  }
  .letterhead {
    position: absolute;
    left: 70px;
    top: 20px;
    width: 820px;
    height: 1160px;
    background: var(--paper);
  }
  .brand {
    position: absolute;
    top: 104px;
    right: 70px;
    display: flex;
    align-items: center;
    gap: 10px;
  }
  .brand-dot {
    width: 14px;
    height: 14px;
    border-radius: 50%;
    background: var(--brand-teal);
  }
  .brand-name {
    font-family: "Open Sans", Arial, sans-serif;
    font-weight: 600;
    font-size: 26px;
    letter-spacing: -0.5px;
    color: var(--ink);
    text-transform: uppercase;
  }
  .contact-seal {
    position: absolute;
    left: 92px;
    bottom: 58px;
    width: 176px;
    height: 176px;
    border-radius: 50%;
    background: var(--tint-pale);
    display: flex;
    align-items: center;
    justify-content: center;
  }
  .contact-details {
    font-family: "Open Sans", Arial, sans-serif;
    font-style: normal;
    font-weight: 400;
    font-size: 11px;
    line-height: 1.35;
    color: var(--ink-soft);
    text-align: right;
  }
</style>
</head>
<body>
  <main class="canvas">
    <section class="letterhead" aria-label="Keyhaven Estates A4 letterhead">
      <header class="brand">
        <span class="brand-name">Keyhaven Estates</span>
        <span class="brand-dot" aria-hidden="true"></span>
      </header>

      <footer class="contact-seal">
        <address class="contact-details">
          Suite 7<br>
          18-19 Harlow Parade<br>
          Brookvale NSW 2100<br>
          Tel: Tom Carrick 0417 293 608<br>
          Lorena Adcock 0409 516 742<br>
          www.keyhavenestatesgroup.com.au
        </address>
      </footer>
    </section>
  </main>
</body>
</html>
```